RM Cargoline businesscard project

RM Cargoline Ltd is a freshly founded small (3 employees), young (average age is 30 years) company, living from the road transportation market without own tools.
We would like to have an impressive, new-line, cool busines card for a freshly founded forwarding company on an overcrowded market which raises attention and makes the potential partners eager to work with us.

Target Market(s)

The main profile of the company is logistic/forwarding on road.

Industry/Entity Type

Freight Forwarding

Contact Information for Business Card

Name: Berki Zsófia
Title: general manager
mobile nr: +36-70/482-5193
fax nr: +36-1/534-9061
e-mail: zsofia.berki@rmcargoline.example
info@rmcargoline.example
website address: http://www.rmcargoline.example
and if possible maybe some funny or helpful info on the back

Requirements
Must have
• contact details above
Nice to have
• some really nice and catching back-side (info, graphics, useful tool info... anything)
Should not have
• trucks, road, ship, airplane on it...

```html
<!DOCTYPE html>
<html lang="en">
<head>
<meta charset="utf-8">
<title>RM Cargoline – Business Card</title>
<link rel="stylesheet" href="https://fonts.googleapis.com/css2?family=Oswald:wght@500&family=Open+Sans:wght@400;600&display=swap">
<style>
  :root {
    --page: #e9e6e1;
    --card-white: #f5f7f8;
    --navy: #1e3343;
    --navy-line: #4a6478;
    --blue: #2f7aa8;
    --blue-light: #7faac8;
    --name-blue: #3d7fb5;
    --ink: #1f1f1f;
    --ink-soft: #4a4f55;
    --on-dark: #e8eef2;
  }
  * { box-sizing: border-box; margin: 0; padding: 0; }
  html, body {
    width: 1200px; height: 800px; overflow: hidden;
    background: var(--page);
    font-family: "Open Sans", Arial, sans-serif;
  }
  .sheet { position: relative; width: 1200px; height: 800px; }
  .card {
    position: absolute; top: 245px;
    width: 530px; height: 310px;
    background: var(--card-white);
    box-shadow: 0 6px 18px rgba(0,0,0,.18);
    overflow: hidden;
  }
  .card--front { left: 50px; }
  .card--back { left: 620px; }
  .card__art { position: absolute; inset: 0; width: 530px; height: 310px; }

  .name-band { position: absolute; left: 42px; top: 34px; }
  .name-band__name {
    font-size: 17px; font-weight: 400; letter-spacing: .5px;
    color: var(--name-blue); text-transform: uppercase; line-height: 1.1;
  }
  .name-band__title {
    font-size: 8.5px; font-weight: 600; letter-spacing: .6px;
    color: var(--ink-soft); text-transform: uppercase;
  }

  .contact-list { position: absolute; left: 42px; top: 104px; list-style: none; }
  .contact-list__item {
    display: flex; align-items: center; gap: 10px;
    height: 22px; margin-bottom: 12px;
  }
  .contact-list__icon {
    width: 20px; height: 20px; flex: none;
    background: var(--blue); border-radius: 2px;
    display: flex; align-items: center; justify-content: center;
  }
  .contact-list__text {
    font-size: 9.5px; line-height: 1.25; color: var(--on-dark);
  }
  .contact-list__web {
    position: absolute; left: 42px; top: 207px;
    font-size: 9.5px; color: var(--on-dark);
  }

  .brand {
    position: absolute; display: flex; align-items: center; gap: 10px;
    font-family: "Oswald", "Arial Narrow", sans-serif; font-weight: 500;
    color: var(--ink); white-space: nowrap;
  }
  .brand__square { background: var(--blue); flex: none; }
  .card--front .brand { left: 308px; top: 156px; font-size: 26px; }
  .card--front .brand__square { width: 20px; height: 20px; }
  .card--back .brand { left: 50%; top: 50%; transform: translate(-50%, -50%); font-size: 34px; }
  .card--back .brand__square { width: 26px; height: 26px; }
</style>
</head>
<body>
<main class="sheet">

  <section class="card card--front" aria-label="Business card, front">
    <svg class="card__art" viewBox="0 0 530 310" aria-hidden="true">
      <polygon points="0,0 345,0 262,122 262,310 0,310" fill="var(--navy)"/>
      <polygon points="330,0 338,0 270,100 270,250 262,250 262,118" fill="var(--blue-light)"/>
      <polygon points="345,0 374,0 291,126 291,310 262,310 262,122" fill="var(--blue)"/>
      <line x1="318" y1="40" x2="258" y2="130" stroke="var(--navy-line)" stroke-width="1"/>
      <line x1="248" y1="150" x2="248" y2="300" stroke="var(--navy-line)" stroke-width="1"/>
      <line x1="392" y1="8" x2="378" y2="30" stroke="var(--blue)" stroke-width="1.5"/>
      <polygon points="28,28 318,28 285,80 28,80" fill="var(--card-white)"/>
    </svg>

    <div class="name-band">
      <p class="name-band__name">Berki Zsófia</p>
      <p class="name-band__title">General Manager</p>
    </div>

    <ul class="contact-list">
      <li class="contact-list__item">
        <span class="contact-list__icon">
          <svg width="12" height="12" viewBox="0 0 24 24" aria-hidden="true"><path fill="#fff" d="M6.6 10.8a15 15 0 0 0 6.6 6.6l2.2-2.2a1 1 0 0 1 1-.25 11.4 11.4 0 0 0 3.6.57 1 1 0 0 1 1 1V20a1 1 0 0 1-1 1A17 17 0 0 1 3 4a1 1 0 0 1 1-1h3.5a1 1 0 0 1 1 1c0 1.25.2 2.45.57 3.57a1 1 0 0 1-.25 1z"/></svg>
        </span>
        <span class="contact-list__text">mobile nr: +36-70/482-5193<br>fax nr: +36-1/534-9061</span>
      </li>
      <li class="contact-list__item">
        <span class="contact-list__icon">
          <svg width="12" height="12" viewBox="0 0 24 24" aria-hidden="true"><rect x="3" y="5" width="18" height="14" rx="1" fill="none" stroke="#fff" stroke-width="2"/><path d="M3 6l9 7 9-7" fill="none" stroke="#fff" stroke-width="2"/></svg>
        </span>
        <span class="contact-list__text">zsofia.berki@rmcargoline.example<br>info@rmcargoline.example</span>
      </li>
      <li class="contact-list__item">
        <span class="contact-list__icon">
          <svg width="12" height="12" viewBox="0 0 24 24" aria-hidden="true"><circle cx="12" cy="12" r="9" fill="none" stroke="#fff" stroke-width="2"/><path d="M3 12h18M12 3c3 3 3 15 0 18M12 3c-3 3-3 15 0 18" fill="none" stroke="#fff" stroke-width="1.6"/></svg>
        </span>
      </li>
    </ul>
    <p class="contact-list__web">http://www.rmcargoline.example</p>

    <div class="brand"><span class="brand__square"></span>RM Cargoline</div>
  </section>

  <section class="card card--back" aria-label="Business card, back">
    <svg class="card__art" viewBox="0 0 530 310" aria-hidden="true">
      <g class="corner-chevron">
        <polygon points="128,0 152,0 24,92 0,92 0,76" fill="var(--blue)"/>
        <polygon points="112,20 120,20 30,84 12,84 12,82" fill="var(--blue-light)"/>
        <line x1="160" y1="6" x2="160" y2="56" stroke="var(--blue)" stroke-width="1.5"/>
        <line x1="90" y1="90" x2="40" y2="118" stroke="var(--blue)" stroke-width="1"/>
      </g>
      <g class="corner-chevron" transform="rotate(180 265 155)">
        <polygon points="128,0 152,0 24,92 0,92 0,76" fill="var(--blue)"/>
        <polygon points="112,20 120,20 30,84 12,84 12,82" fill="var(--blue-light)"/>
        <line x1="160" y1="6" x2="160" y2="56" stroke="var(--blue)" stroke-width="1.5"/>
        <line x1="90" y1="90" x2="40" y2="118" stroke="var(--blue)" stroke-width="1"/>
      </g>
    </svg>
    <div class="brand"><span class="brand__square"></span>RM Cargoline</div>
  </section>

</main>
</body>
</html>
```